Bref créative
Business Cards and Stationary for Real Estate Firm
Maple Crest Realty Group
Professional
Dennis R. Holloway
Broker/Owner
4782 Lantern Hill Rd
Suite 308
Cedarbrook, OR 95862
dholloway@brightharborfirm.com
www.maplecrestrealtygroup.net
DRE # 02947716
There should be a place for a photo of the agent on the front of the card, but can work fine if the agent does not put their photo on it. These card designs will be used for multiple agents, I assume the name, phone numbers, email address, etc can be changed for each agent. The AI files and any others that may be needed are in the uploaded zip file.
The back of the card may be a tag line or some other kind of message.
Files in black and white, and with color.

```html
<!DOCTYPE html>
<html lang="en">
<head>
<meta charset="utf-8">
<title>Maple Crest Realty Group — Business Cards</title>
<link href="https://fonts.googleapis.com/css2?family=Cinzel:wght@400;600&family=EB+Garamond:wght@400;500&display=swap" rel="stylesheet">
<style>
  :root {
    --brand-red: #c8363b;
    --brand-red-deep: #b02e33;
    --paper: #ffffff;
    --paper-shade: #eeeeee;
    --stage: #e4e4e2;
    --ink-soft: #f6dede;
  }
  * { box-sizing: border-box; margin: 0; padding: 0; }
  html, body { width: 1200px; height: 838px; overflow: hidden; }
  body {
    background: var(--stage);
    position: relative;
    font-family: "EB Garamond", Georgia, serif;
  }
  .card {
    position: absolute;
    width: 520px;
    height: 298px;
    box-shadow: 0 10px 24px rgba(0,0,0,0.18);
    overflow: hidden;
  }

  /* Back of card */
  .card-back {
    left: 600px;
    top: 110px;
    background: var(--brand-red);
    display: flex;
    flex-direction: column;
    align-items: center;
    justify-content: center;
    gap: 18px;
    color: var(--paper);
  }
  .back-mark {
    display: flex;
    align-items: center;
    gap: 14px;
  }
  .back-mark .mark-dot {
    width: 22px; height: 22px;
    border-radius: 50%;
    background: var(--paper);
  }
  .back-mark .mark-name {
    font-family: "Cinzel", "Times New Roman", serif;
    font-weight: 400;
    font-size: 26px;
    letter-spacing: 1px;
    color: var(--paper);
  }
  .back-web {
    font-family: "Cinzel", "Times New Roman", serif;
    font-size: 15px;
    letter-spacing: 2px;
    text-transform: uppercase;
  }

  /* Front of card */
  .card-front {
    left: 80px;
    top: 440px;
    background: var(--paper);
    display: flex;
  }
  .front-brand {
    width: 212px;
    height: 100%;
    display: flex;
    flex-direction: column;
    align-items: center;
    justify-content: center;
    gap: 12px;
    text-align: center;
  }
  .front-brand .mark-dot {
    width: 16px; height: 16px;
    border-radius: 50%;
    background: var(--brand-red);
  }
  .front-brand .mark-name {
    font-family: "Cinzel", "Times New Roman", serif;
    font-weight: 400;
    font-size: 19px;
    line-height: 1.25;
    color: var(--brand-red);
    letter-spacing: 0.5px;
  }
  .front-details {
    flex: 1;
    height: 100%;
    background: var(--brand-red);
    position: relative;
    padding: 30px 48px 0 22px;
    color: var(--paper);
  }
  .front-details .edge-strip {
    position: absolute;
    top: 0; right: 18px;
    width: 9px; height: 100%;
    background: var(--paper-shade);
  }
  .agent-name {
    font-family: "Cinzel", "Times New Roman", serif;
    font-size: 15px;
    letter-spacing: 0.5px;
  }
  .agent-title {
    font-family: "Cinzel", "Times New Roman", serif;
    font-size: 9px;
    letter-spacing: 1px;
    margin-top: 3px;
  }
  .rule {
    height: 2px;
    background: var(--paper);
    margin: 12px -22px 22px -22px;
    width: calc(100% + 22px);
  }
  .contact-list { list-style: none; display: flex; flex-direction: column; gap: 4px; }
  .contact-list li {
    display: flex;
    align-items: center;
    gap: 7px;
    font-size: 10.5px;
    letter-spacing: 0.4px;
    line-height: 1.2;
    white-space: nowrap;
  }
  .contact-list .icon {
    width: 11px; height: 11px; flex: none;
  }
  .contact-list .plain { padding-left: 18px; }
  .license {
    margin-top: 8px;
    font-size: 9px;
    letter-spacing: 1px;
    color: var(--ink-soft);
  }
</style>
</head>
<body>

  <section class="card card-back" aria-label="Business card back">
    <div class="back-mark">
      <span class="mark-dot"></span>
      <span class="mark-name">Maple Crest Realty Group</span>
    </div>
    <div class="back-web">www.maplecrestrealtygroup.net</div>
  </section>

  <section class="card card-front" aria-label="Business card front">
    <div class="front-brand">
      <span class="mark-dot"></span>
      <span class="mark-name">Maple Crest<br>Realty Group</span>
    </div>
    <div class="front-details">
      <div class="agent-name">Dennis R. Holloway</div>
      <div class="agent-title">Broker/Owner</div>
      <div class="rule"></div>
      <ul class="contact-list">
        <li>
          <svg class="icon" viewBox="0 0 12 12"><circle cx="6" cy="6" r="6" fill="#fff"/><path d="M6 2.5a2.2 2.2 0 0 0-2.2 2.2C3.8 6.4 6 9.5 6 9.5s2.2-3.1 2.2-4.8A2.2 2.2 0 0 0 6 2.5z" fill="#c8363b"/></svg>
          4782 Lantern Hill Rd
        </li>
        <li class="plain">Suite 308</li>
        <li class="plain">Cedarbrook, OR 95862</li>
        <li>
          <svg class="icon" viewBox="0 0 12 12"><circle cx="6" cy="6" r="6" fill="#fff"/><path d="M4 3h1.3l.6 1.6-.8.6a4 4 0 0 0 1.7 1.7l.6-.8 1.6.6V8a1 1 0 0 1-1 1A5 5 0 0 1 3 4a1 1 0 0 1 1-1z" fill="#c8363b"/></svg>
          O: (555) 014-2281
        </li>
        <li>
          <svg class="icon" viewBox="0 0 12 12"><circle cx="6" cy="6" r="6" fill="#fff"/><path d="M4 3h1.3l.6 1.6-.8.6a4 4 0 0 0 1.7 1.7l.6-.8 1.6.6V8a1 1 0 0 1-1 1A5 5 0 0 1 3 4a1 1 0 0 1 1-1z" fill="#c8363b"/></svg>
          C: (555) 019-8834
        </li>
        <li>
          <svg class="icon" viewBox="0 0 12 12"><circle cx="6" cy="6" r="6" fill="#fff"/><rect x="3" y="4" width="6" height="4.2" fill="none" stroke="#c8363b" stroke-width="0.9"/><path d="M3 4l3 2.3L9 4" fill="none" stroke="#c8363b" stroke-width="0.9"/></svg>
          dholloway@brightharborfirm.com
        </li>
        <li>
          <svg class="icon" viewBox="0 0 12 12"><circle cx="6" cy="6" r="6" fill="#fff"/><circle cx="6" cy="6" r="3" fill="none" stroke="#c8363b" stroke-width="0.9"/><path d="M3 6h6M6 3c-1.3 1.6-1.3 4.4 0 6M6 3c1.3 1.6 1.3 4.4 0 6" fill="none" stroke="#c8363b" stroke-width="0.7"/></svg>
          www.maplecrestrealtygroup.net
        </li>
      </ul>
      <div class="license">DRE # 02947716</div>
      <div class="edge-strip"></div>
    </div>
  </section>

</body>
</html>
```